Restaurant Menu Design

We are a Steak & Seafood restaurant (Silver Hollow Steak & Seafood Co.). We are located in Lake Placid, NY in the heart of the Adirondack Mountains. We are a restaurant and award winning brewery. We are a rustic style restaurant with a dark wood decor and antique's adding to the atmosphere. Our beer selection is mostly Ales and some seasonal lagers. The website for better a idea is brambleridgeale.example. I'm adding a .pub file with our current menus for sizing. They are set to legal document. Our specialty is slow roasted prime rib. We also have a lobster tank which we feature. Our menus have 4 standard legal size (front/back) and a half legal for our specials list.
Updates
Just an update on the menu, we will need the cover page, then the two inside slots would be the food pages and the welcome page/family outline page would go on the back. The drink menu will be placed into a different insert. We also don't need all the graphics we have on our old menu. They were just used as fillers in this menu.
Reason: We will be extending the deadline since the PDFs of the menus haven't been properly uploaded. They will be uploaded shortly
Just an update the PDF of the menu has been uploaded. It should be on the top of the files lists. ALso the deadline has been extended 5 days
Target Market(s)
Middle to high income earners
Industry/Entity Type
Restaurant
Look and feel

```html
<!DOCTYPE html>
<html lang="en">
<head>
<meta charset="utf-8">
<title>Silver Hollow Steak &amp; Seafood – Menu Back Page</title>
<link href="https://fonts.googleapis.com/css2?family=Open+Sans:wdth,wght@75..100,400..800&family=Arimo:wght@700&display=swap" rel="stylesheet">
<style>
  :root {
    --backdrop: #c94f95;
    --paper: #fdfbf3;
    --border-stripe-a: #ece4d2;
    --border-stripe-b: #f7f2e6;
    --ink: #1b1b1b;
    --ornament: #a0625f;
    --photo-frame: #1a1a1a;
    --photo-tone-a: #9a9a92;
    --photo-tone-b: #4a4a44;
    --beer-panel: #8c3f45;
    --beer-panel-line: #a6585e;
    --beer-text: #ffffff;
    --beer-photo-a: #c99a55;
    --beer-photo-b: #5e3f2b;
  }
  html, body { margin: 0; padding: 0; }
  body {
    width: 745px; height: 1200px; overflow: hidden; position: relative;
    background: var(--backdrop);
    font-family: "Open Sans", Arial, sans-serif;
    color: var(--ink);
  }
  .menu-page {
    position: absolute; left: 88px; top: 122px;
    width: 569px; height: 955px;
    background: var(--paper);
    box-shadow: 0 0 4px rgba(0,0,0,.25);
  }
  .menu-page::before, .menu-page::after {
    content: ""; position: absolute; top: 0; bottom: 0; width: 22px;
    background: repeating-linear-gradient(180deg, var(--border-stripe-a) 0 6px, var(--border-stripe-b) 6px 12px);
  }
  .menu-page::before { left: 0; }
  .menu-page::after { right: 0; }
  .abs { position: absolute; }
  .page-title {
    left: 0; width: 100%; margin: 0; text-align: center;
    font-weight: 800; font-size: 26px; line-height: 35px;
  }
  .flourish {
    left: 228px; width: 112px; height: 10px;
    background: var(--ornament); border-radius: 5px; opacity: .55;
  }
  .heritage-photo {
    left: 130px; top: 110px; width: 308px; height: 212px;
    box-sizing: border-box; border: 8px solid var(--photo-frame);
    background: linear-gradient(135deg, var(--photo-tone-a), var(--photo-tone-b));
  }
  .tagline { left: 0; width: 100%; top: 329px; margin: 0; text-align: center; font-weight: 700; font-size: 17px; line-height: 24px; }
  .contact { left: 0; width: 100%; margin: 0; text-align: center; font-weight: 700; font-size: 12.5px; line-height: 17px; }
  .body-copy { left: 46px; width: 478px; margin: 0; font-stretch: 87%; }
  .body-copy .line { display: block; text-align: justify; text-align-last: justify; }
  .body-copy .line.end { text-align-last: left; }
  .welcome { top: 458px; font-size: 10px; line-height: 13.5px; }
  .brewery-title { left: 46px; top: 593px; margin: 0; font-weight: 800; font-size: 26px; line-height: 35px; }
  .brewery-text { top: 625px; font-size: 10.8px; line-height: 16.5px; font-stretch: 90%; }
  .beer-panel {
    left: 46px; top: 703px; width: 477px; height: 182px;
    background: var(--beer-panel);
  }
  .beer-panel .rules {
    position: absolute; left: 122px; top: 6px; width: 219px; height: 36px;
    background: repeating-linear-gradient(180deg, transparent 0 8px, var(--beer-panel-line) 8px 9px);
  }
  .beer-list, .brewery-extras {
    margin: 0; padding: 0; list-style: none;
    font-family: "Arimo", Arial, sans-serif; font-weight: 700;
    font-size: 14px; line-height: 17px; color: var(--beer-text);
  }
  .beer-list { position: absolute; left: 17px; top: 13px; }
  .brewery-extras { position: absolute; left: 354px; top: 13px; width: 122px; }
  .beer-photo {
    position: absolute; left: 122px; top: 42px; width: 219px; height: 120px;
    background: linear-gradient(180deg, var(--beer-photo-a), var(--beer-photo-b));
  }
</style>
</head>
<body>
  <main class="menu-page">
    <h1 class="abs page-title" style="top:53px">SILVER HOLLOW STEAK &amp; SEAFOOD</h1>
    <div class="abs flourish" style="top:87px" role="img" aria-label="Decorative scroll ornament"></div>

    <div class="abs heritage-photo" role="img" aria-label="Vintage sepia photograph of gentlemen in bowler hats sharing beers around a table outside a tavern"></div>

    <p class="abs tagline">Great Food * Great Beer &nbsp;Great People</p>
    <p class="abs contact" style="top:352px">www.silverhollowsteak.example</p>
    <p class="abs contact" style="top:369px">hello@silverhollow.example</p>

    <h2 class="abs page-title" style="top:402px">SILVER HOLLOW STEAK &amp; SEAFOOD</h2>
    <div class="abs flourish" style="top:442px" role="img" aria-label="Decorative scroll ornament"></div>

    <div class="abs body-copy welcome">
      <span class="line end">Welcome!!</span>
      <span class="line">The Harlow Family has owned and operated The Silver Hollow Steak &amp; Seafood since 1987. Moving</span>
      <span class="line">from New Jersey, Walt and Ruth thought it would be "fun" to completely renovate a building and</span>
      <span class="line">establish a quality restaurant with their children. Their idea of the good life is chatting to the people</span>
      <span class="line end">that come in and making sure their guests get great service, food and beer.</span>
      <span class="line">While enjoying your meals, please take the time to notice Walt's extensive assortment of antiques. He has</span>
      <span class="line end">been collecting his "finds" for longer than most of us have been alive.</span>
      <span class="line end">All of us here sincerely hope you enjoy your time with us and trust you will join us again.</span>
    </div>

    <h2 class="abs brewery-title">BRAMBLE RIDGE BREWING CO.</h2>
    <div class="abs body-copy brewery-text">
      <span class="line">In 1996, the Harlow Family decided to start making their own beer. The brewery is now located</span>
      <span class="line">behind the restaurant, and all the beers on tap are made on the premises. The beers produced</span>
      <span class="line">in our small brewery have won a number of prestigious awards at national and state beer</span>
      <span class="line end">competitions.</span>
    </div>

    <section class="abs beer-panel">
      <div class="rules"></div>
      <ul class="beer-list">
        <li>Iron Miller</li>
        <li>Pale Ale</li>
        <li>Ridgeline</li>
        <li>Abbey</li>
        <li>Hayloft</li>
        <li>Blonde Ale</li>
        <li>Cedar Wolf</li>
        <li>Red Ale</li>
        <li>Old Tyme Root</li>
      </ul>
      <div class="beer-photo" role="img" aria-label="Photo of a growler and a row of sampler glasses of house beers on a wooden bar"></div>
      <ul class="brewery-extras">
        <li>Souvenir</li>
        <li>pint glasses.</li>
        <li>Fill a growler.</li>
        <li>Beer Samplers.</li>
        <li>Ask about our</li>
        <li>seasonal beers</li>
        <li>on tap today.</li>
        <li>Personal tours of</li>
        <li>our brewery avail-</li>
      </ul>
    </section>

    <div class="abs flourish" style="top:903px" role="img" aria-label="Decorative scroll ornament"></div>
  </main>
</body>
</html>
```